Create Business Cards for Technology Company

I need to get business cards created for my technology company. I have included our business logo. Once the winning design is selected I can provide you with the Adobe Illustrator or PDF version of the logo file so that you can finalize the cards. The business cards will be front and back and will include the following information:

Front of Card:

Company Name

Name of Person
Position

P: (xxx) xxx-xxxx
E: xxxxx@[url removed, login to view]

Back of Card:

Consulting Services:
Web Design, Mobile Applications, Search Marketing,
Social Media, Analytics, Email Marketing

```html
<!DOCTYPE html>
<html lang="en">
<head>
<meta charset="utf-8">
<title>Business Card – Front and Back</title>
<link href="https://fonts.googleapis.com/css2?family=Oswald:wght@500&family=Open+Sans:wght@400&display=swap" rel="stylesheet">
<style>
  :root {
    --stage: #e6e7e9;
    --paper: #ffffff;
    --paper-shade: #eceded;
    --frame: #3a3b3d;
    --accent: #39b4e4;
    --ink: #3d3e40;
    --ink-soft: #6a6b6d;
    --dot: #e0322f;
    --rule: #8c8d8f;
  }
  html, body {
    margin: 0;
    padding: 0;
    width: 1200px;
    height: 2577px;
    overflow: hidden;
    background: var(--stage);
  }
  .sheet {
    position: relative;
    width: 1200px;
    height: 2577px;
  }
  .card {
    position: absolute;
    left: 100px;
    width: 1000px;
    height: 571px;
    box-shadow: 0 18px 40px rgba(0,0,0,0.22);
  }
  .card--front { top: 560px; }
  .card--back { top: 1450px; }
  .card svg { display: block; }
  .heading { font-family: 'Oswald', sans-serif; font-weight: 500; fill: var(--ink); }
  .body { font-family: 'Open Sans', sans-serif; font-weight: 400; fill: var(--ink-soft); }
  .frame { fill: var(--frame); }
  .accent { fill: var(--accent); }
</style>
</head>
<body>
<main class="sheet">

  <section class="card card--front" aria-label="Card front">
    <svg width="1000" height="571" viewBox="0 0 1000 571">
      <defs>
        <linearGradient id="paperFront" x1="0" y1="0" x2="1" y2="1">
          <stop offset="0" stop-color="var(--paper-shade)"/>
          <stop offset="0.5" stop-color="var(--paper)"/>
          <stop offset="1" stop-color="var(--paper-shade)"/>
        </linearGradient>
      </defs>
      <rect class="paper" width="1000" height="571" fill="url(#paperFront)"/>
      <polygon class="frame" points="0,0 860,0 895,38 0,38"/>
      <polygon class="accent" points="850,0 1000,0 1000,62 930,62 895,38 880,38"/>
      <rect class="frame" x="0" y="0" width="20" height="571"/>
      <polygon class="accent" points="0,395 210,395 210,470 252,571 0,571"/>
      <polygon class="frame" points="228,528 1000,528 1000,571 252,571"/>

      <g class="brand">
        <circle cx="125" cy="168" r="34" fill="var(--dot)"/>
        <text class="heading" x="60" y="262" font-size="46">COMPANY NAME</text>
      </g>

      <g class="identity" text-anchor="end">
        <text class="heading" x="930" y="128" font-size="44">JOHN DOE</text>
        <text class="body" x="930" y="158" font-size="19">Graphic Designer</text>
      </g>

      <g class="contact" font-size="19">
        <g class="contact-web">
          <circle cx="733" cy="329" r="8" fill="none" stroke="var(--ink)" stroke-width="2"/>
          <line x1="725" y1="329" x2="741" y2="329" stroke="var(--ink)" stroke-width="1.5"/>
          <text class="body" x="755" y="336">www.yourwebsite.com</text>
        </g>
        <g class="contact-phone">
          <path d="M729 363 q8 7 0 16" fill="none" stroke="var(--ink)" stroke-width="3" stroke-linecap="round"/>
          <text class="body" x="755" y="377">+(000) 1234-5678</text>
        </g>
        <g class="contact-mail">
          <rect x="724" y="406" width="18" height="13" fill="none" stroke="var(--ink)" stroke-width="1.8"/>
          <path d="M724 406 l9 7 l9 -7" fill="none" stroke="var(--ink)" stroke-width="1.8"/>
          <text class="body" x="755" y="418">johndoe@email.com</text>
        </g>
      </g>
    </svg>
  </section>

  <section class="card card--back" aria-label="Card back">
    <svg width="1000" height="571" viewBox="0 0 1000 571">
      <defs>
        <linearGradient id="paperBack" x1="0" y1="0" x2="1" y2="1">
          <stop offset="0" stop-color="var(--paper-shade)"/>
          <stop offset="0.5" stop-color="var(--paper)"/>
          <stop offset="1" stop-color="var(--paper-shade)"/>
        </linearGradient>
      </defs>
      <rect class="paper" width="1000" height="571" fill="url(#paperBack)"/>
      <polygon class="frame" points="0,0 830,0 865,38 0,38"/>
      <polygon class="accent" points="820,0 1000,0 1000,90 955,90 905,38 850,38"/>
      <rect class="frame" x="0" y="0" width="26" height="571"/>
      <rect class="frame" x="974" y="90" width="26" height="481"/>
      <polygon class="accent" points="0,315 40,315 110,430 40,530 0,530"/>
      <rect class="frame" x="0" y="533" width="1000" height="38"/>

      <text class="heading" x="500" y="128" font-size="40" text-anchor="middle">CONSULTING SERVICES</text>

      <g class="service-map">
        <g stroke="var(--rule)" stroke-width="4">
          <line x1="90" y1="232" x2="218" y2="232"/>
          <line x1="242" y1="232" x2="368" y2="232"/>
          <line x1="392" y1="232" x2="548" y2="232"/>
          <line x1="572" y1="232" x2="718" y2="232"/>
          <line x1="742" y1="232" x2="910" y2="232"/>
          <line x1="490" y1="290" x2="490" y2="308"/>
          <line x1="490" y1="332" x2="490" y2="368"/>
          <line x1="490" y1="392" x2="490" y2="440"/>
        </g>
        <g fill="var(--dot)">
          <circle cx="230" cy="232" r="9"/>
          <circle cx="380" cy="232" r="9"/>
          <circle cx="560" cy="232" r="9"/>
          <circle cx="730" cy="232" r="9"/>
          <circle cx="490" cy="320" r="9"/>
          <circle cx="490" cy="380" r="9"/>
        </g>
        <g class="body" font-size="19">
          <text x="200" y="208" text-anchor="middle">Web Design</text>
          <text x="380" y="268" text-anchor="middle">Mobile Applications</text>
          <text x="560" y="208" text-anchor="middle">Social Media</text>
          <text x="745" y="268" text-anchor="middle">Analytics</text>
          <text x="512" y="326">Search Marketing</text>
          <text x="468" y="386" text-anchor="end">Email Marketing</text>
        </g>
      </g>
    </svg>
  </section>

</main>
</body>
</html>
```